Wochen Speiseplan
Zielgruppe
Hospiz
Aufgabenstellung
Wir brauchen für unser Hospiz einen Wochenspeiseplan. Es soll eine Powerpointseite im A4 Format erstellt werden. Wir brauchen 4 unterschiedliche Seiten - für jede Jahreszeit einen Entwurf. Der Speiseplan soll von uns selbst ausgefüllt werden können.
Inhalte: Montag - Sonntag jeweils Mittag- und Abendessen. (Aufgebaut wie ein Stundenplan.). Möglichst große Schriftgröße. In der Fußnote bitte: "Änderungen vorbehalten schreiben". Das ganze soll professionell, aber dennoch liebevoll gestaltet sein. Es soll unseren Bewohnern "Liust machen" draufzuschauen. Der Plan wird jede Woche neu ausgefüllt, ausgedruckt und laminiert. Sollte also einfach zu handhaben sein.
Das Hospiz lebt von Spenden, daher bitte nicht zu aufwendig, dafür aber bezahlbar machen.

```html
<!DOCTYPE html>
<html lang="de">
<head>
<meta charset="utf-8">
<title>Wochenspeiseplan Winter</title>
<link rel="stylesheet" href="https://fonts.googleapis.com/css2?family=Sniglet:wght@400;800&family=Delius&family=PT+Sans:ital,wght@0,400;0,700;1,700&display=swap">
<style>
  :root {
    --sky-pale: #dbeaf5;
    --sky-mid: #b9d8ee;
    --banner: #55b6e6;
    --navy: #243a5c;
    --row-light: #dce6f2;
    --row-dark: #a8c2e2;
    --ink: #1a1a1a;
    --white: #ffffff;
  }
  * { margin: 0; padding: 0; box-sizing: border-box; }
  html, body { width: 1200px; height: 900px; overflow: hidden; }
  body { font-family: "PT Sans", Arial, sans-serif; color: var(--ink); }

  .menu-board {
    position: relative;
    width: 1200px;
    height: 900px;
    overflow: hidden;
    background: var(--sky-pale);
  }
  .snow-pattern {
    position: absolute;
    inset: 0;
    background: radial-gradient(ellipse at 20% 30%, var(--sky-mid), transparent 60%),
                radial-gradient(ellipse at 85% 80%, var(--sky-mid), transparent 55%),
                linear-gradient(160deg, #cfe3f3, var(--sky-pale) 60%, #c7def0);
  }
  .title-banner { position: absolute; left: 0; top: 0; width: 1200px; height: 280px; }

  .title {
    position: absolute;
    left: 262px;
    top: 52px;
    font-family: "Sniglet", "Arial Rounded MT Bold", sans-serif;
    font-weight: 400;
    font-size: 88px;
    color: var(--white);
    transform: rotate(-4deg);
    transform-origin: left center;
    letter-spacing: 0.5px;
  }
  .greeting {
    position: absolute;
    left: 425px;
    top: 188px;
    font-family: "Delius", Georgia, serif;
    font-size: 27px;
    color: var(--white);
    transform: rotate(-4deg);
    transform-origin: left center;
    letter-spacing: 0.5px;
  }

  .meal-table {
    position: absolute;
    left: 37px;
    top: 258px;
    width: 1130px;
    border-collapse: collapse;
    font-size: 21px;
    line-height: 1.2;
  }
  .meal-table th {
    background: var(--navy);
    color: var(--white);
    font-style: italic;
    font-weight: 700;
    font-size: 25px;
    text-align: left;
    height: 67px;
    padding: 0 12px;
  }
  .meal-table td {
    height: 73px;
    padding: 8px 12px;
    vertical-align: top;
  }
  .meal-table tr:nth-child(odd) td { background: var(--row-light); }
  .meal-table tr:nth-child(even) td { background: var(--row-dark); }
  .meal-table tbody tr + tr td { border-top: 2px solid var(--white); }
  .col-day { width: 177px; }
  .col-lunch { width: 470px; }
  .day { font-weight: 700; font-style: italic; }

  .footnote {
    position: absolute;
    right: 8px;
    top: 850px;
    font-weight: 700;
    font-style: italic;
    font-size: 18px;
  }
</style>
</head>
<body>
<main class="menu-board">
  <div class="snow-pattern" role="img" aria-label="Winterlicher Hintergrund mit weißen Schneeflocken"></div>

  <svg class="title-banner" viewBox="0 0 1200 280" aria-hidden="true">
    <polygon points="242,48 1200,-30 1200,182 262,262" fill="var(--banner)"/>
  </svg>

  <h1 class="title">Wochenspeiseplan</h1>
  <p class="greeting">Wir wünschen einen guten Appetit!</p>

  <table class="meal-table">
    <colgroup>
      <col class="col-day"><col class="col-lunch"><col>
    </colgroup>
    <thead>
      <tr><th></th><th>Mittagessen</th><th>Abendessen</th></tr>
    </thead>
    <tbody>
      <tr><td class="day">Montag</td><td>Spaghetti Bolognese</td><td>Gemüsepfanne mit Hähnchenbrust</td></tr>
      <tr><td class="day">Dienstag</td><td>Chicken Wrap mit buntem Salat<br>und Guacamole</td><td>Gebratener Seehecht in Ei-Hülle<br>dazu Kartoffelpüree</td></tr>
      <tr><td class="day">Mittwoch</td><td>Milchreis mit Zucker/Zimt<br>und Kirschkompott</td><td>Frikadelle schwäbische Art auf<br>Kräuterspätzle</td></tr>
      <tr><td class="day">Donnerstag</td><td>Nudeleintopf mit Geflügelfleisch</td><td>Gegrillte Schweinshaxe</td></tr>
      <tr><td class="day">Freitag</td><td>Germknödel mit Pflaumenmusfüllung</td><td>Nudel-Schinken-Gratin dazu<br>gemischter Salat</td></tr>
      <tr><td class="day">Samstag</td><td>3 gekochte Eier mit Senfsoße und<br>Kartoffeln</td><td>Kartoffelrösti mit Tomaten-Schnittlauch-<br>Quark</td></tr>
      <tr><td class="day">Sonntag</td><td>Linseneintopf mit Bockwurst,<br>Fladenbrot</td><td>Kochklopse Königsberger Art mit<br>Kartoffeln/Reis</td></tr>
    </tbody>
  </table>

  <p class="footnote">Änderungen vorbehalten</p>
</main>
</body>
</html>
```